Crestwave Glow LED - E- Commerce site

We need a website designed for an LED Billboard company that sells:
1) LED Billboards (Sales & Rental)
2) LED Gas Station lights
3) Truss Systems (Sales & Rental)
4) Sound Systems (Sales & Rental)

Attached are websites that sell similar products as Crestwave Glow LED. Target market is for business, property managers and event coordinators.
This site will need to be an e-commerce site where customers can purchase the product directly from the site. What I'm looking for is a design layout to start.

Conceptual Web Designs:
http://198.51.100.47:8087/index.html
http://www.vomilux-example.com/
http://www.tonarvoxaudio-example.com/
http://www.pelmoraboard-example.com/

Attached is the logo of the company: Please note that the new spelling of the logo is "Crestwave Glow LED" using domain " CrestwaveGlowLED.com

Industry/Entity Type

Gas Station

Number of Pages Required

5+ page

Requirements
Must have
• 1) E-Commerce - Customers will need to be able to order product from the site.
• 2) Customers will also have the option to rent the product as well.
Nice to have
• I like the image of the attached website, that has a video clip loop
• http://www.pelmoraboard-example.com/

```html
<!DOCTYPE html>
<html lang="en">
<head>
<meta charset="utf-8">
<title>Crestwave Glow LED – Home</title>
<link href="https://fonts.googleapis.com/css2?family=Oswald:wght@400;500;600&family=Open+Sans:wght@400;600;700&display=swap" rel="stylesheet">
<style>
:root{
  --red:#e8262b;
  --red-dark:#c81c21;
  --dark:#2f3033;
  --darker:#232427;
  --nav:#3a3b3e;
  --page:#ececec;
  --white:#ffffff;
  --text:#444;
  --muted:#8a8a8a;
  --line:#dcdcdc;
  --green:#2fb87c;
  --teal:#17a2b8;
  --yellow:#f5c400;
}
*{box-sizing:border-box;margin:0;padding:0}
html,body{width:857px;height:1200px;overflow:hidden}
body{background:var(--page);font-family:"Open Sans",Arial,sans-serif;color:var(--text);font-size:9px}
.page{position:relative;width:857px;height:1200px;}
.wrap{width:790px;margin:0 auto}

/* top bar */
.topbar{height:20px;display:flex;align-items:center;justify-content:space-between;font-size:7.5px;text-transform:uppercase}
.topbar .welcome{color:var(--red);font-weight:600}
.topbar .links{color:#666;display:flex;gap:6px}
.topbar .links span+span:before{content:"|";margin-right:6px;color:#bbb}

/* header */
.header{height:44px;display:flex;align-items:center;justify-content:space-between}
.brand{display:flex;align-items:center;gap:7px}
.brand-dot{width:26px;height:26px;border-radius:50%;background:var(--yellow)}
.brand-name{font-family:"Oswald",sans-serif;font-weight:500;font-size:15px;color:var(--red)}
.header-tools{display:flex;align-items:center;gap:8px}
.search{display:flex;height:22px}
.search-field{width:170px;border:1px solid var(--line);background:var(--white);font-size:7.5px;color:#aaa;padding:0 7px;display:flex;align-items:center}
.search-btn{width:24px;background:var(--red);display:flex;align-items:center;justify-content:center}
.cart-btn{height:22px;background:var(--red);color:var(--white);font-size:7.5px;font-weight:600;display:flex;align-items:center;gap:5px;padding:0 9px;text-transform:uppercase}

/* nav */
.navrow{display:flex;height:24px}
.side-title{width:194px;background:var(--red);color:var(--white);font-family:"Oswald",sans-serif;font-size:11px;font-weight:500;display:flex;align-items:center;padding-left:12px;letter-spacing:.5px}
.mainnav{flex:1;background:var(--nav);display:flex;margin-left:6px}
.mainnav a{color:var(--white);text-decoration:none;font-family:"Oswald",sans-serif;font-size:8.5px;letter-spacing:.5px;width:80px;display:flex;align-items:center;justify-content:center}
.mainnav a.active{background:var(--red)}

/* body top */
.top{display:flex;gap:6px;margin-top:6px}
.sidebar{width:194px;background:var(--white);height:367px;padding:4px 0}
.sidebar li{list-style:none;height:22.5px;border-bottom:1px solid #efefef;display:flex;align-items:center;padding-left:14px;font-size:8px;color:#555}
.sidebar li:before{content:"";width:0;height:0;border-left:3px solid var(--red);border-top:3px solid transparent;border-bottom:3px solid transparent;margin-right:7px}
.feature{flex:1;display:flex;flex-direction:column;gap:6px}
.hero{position:relative;height:236px;background:radial-gradient(ellipse at 50% 40%,#2f7a4a 0%,#16333a 40%,#0a0f1d 80%)}
.hero-play{position:absolute;left:50%;top:44%;transform:translate(-50%,-50%)}
.hero-caption{position:absolute;left:24px;bottom:22px;color:var(--white);font-family:"Oswald",sans-serif;font-size:17px;letter-spacing:1px;text-transform:uppercase}
.btn{background:var(--red);color:var(--white);font-family:"Oswald",sans-serif;font-size:9px;letter-spacing:.5px;text-transform:uppercase;padding:6px 14px;display:inline-block}
.hero .btn{position:absolute;right:22px;bottom:20px;font-size:11px;padding:7px 18px}
.promos{display:flex;gap:6px;height:125px}
.promo{flex:1;position:relative;background:#111;color:var(--white);overflow:hidden}
.promo-photo{position:absolute;right:0;top:0;bottom:0;width:46%}
.promo.billboards .promo-photo{background:linear-gradient(135deg,#3c3f44,#d9dadb 55%,#5a5d62)}
.promo.gas .promo-photo{background:linear-gradient(160deg,#0c1a2a,#1f6b4f 60%,#0a0f18)}
.promo-text{position:absolute;left:14px;top:24px;width:52%}
.promo h3{font-family:"Oswald",sans-serif;font-weight:500;font-size:15px;letter-spacing:.5px;text-transform:uppercase}
.promo p{font-size:7.5px;line-height:1.45;margin:4px 0 10px;color:#ddd}
.promo .btn{font-size:7.5px;padding:4px 10px}

/* products */
.section-head{display:flex;justify-content:space-between;align-items:center;margin-top:32px;border-bottom:1px solid var(--line);padding-bottom:6px}
.section-head h2{font-family:"Oswald",sans-serif;font-weight:500;font-size:15px;color:var(--red);letter-spacing:.5px}
.arrows{display:flex;gap:2px}
.arrows span{width:13px;height:13px;background:var(--dark);display:flex;align-items:center;justify-content:center}
.products{display:flex;gap:12px;margin-top:14px}
.card{flex:1;background:var(--white);height:262px;padding:8px}
.card-photo{height:178px;background:linear-gradient(#f6f6f6,#e4e4e4);display:flex;align-items:center;justify-content:center}
.card-info{display:flex;justify-content:space-between;align-items:flex-end;margin-top:10px}
.card-name{font-size:8.5px;color:#333;font-weight:600}
.card-price{font-size:8.5px;color:var(--red);font-weight:700;margin-top:5px}
.card-cart{width:24px;height:24px;background:var(--red);display:flex;align-items:center;justify-content:center}

/* service boxes */
.services{display:flex;gap:12px;margin-top:40px}
.service{flex:1;height:92px;display:flex;align-items:center;gap:14px;padding:0 20px;color:var(--white)}
.service.returns{background:var(--green)}
.service.warranty{background:var(--teal)}
.service.shipping{background:var(--red)}
.service-icon{width:46px;height:46px;flex:none;border:2px solid rgba(255,255,255,.85);border-radius:50%;display:flex;align-items:center;justify-content:center}
.service h4{font-family:"Oswald",sans-serif;font-weight:500;font-size:14px;letter-spacing:1px;text-transform:uppercase}
.service p{font-size:7px;line-height:1.45;margin-top:3px;color:rgba(255,255,255,.9)}

/* footer */
.footer{position:absolute;left:0;right:0;bottom:0;height:186px;background:var(--dark);color:#bbb}
.footer-cols{display:flex;padding-top:22px}
.footer-col{flex:1}
.footer-col h5{font-family:"Oswald",sans-serif;font-weight:500;color:var(--white);font-size:11px;letter-spacing:1px;text-transform:uppercase;margin-bottom:8px}
.footer-col li{list-style:none;font-size:7.5px;line-height:1.85}
.newsletter p{font-size:7.5px;line-height:1.5;margin-bottom:8px}
.subscribe{display:flex;height:18px}
.subscribe .field{width:118px;background:var(--white);font-size:7px;color:#aaa;display:flex;align-items:center;padding-left:6px}
.subscribe .go{background:var(--red);color:var(--white);font-size:7px;padding:0 8px;display:flex;align-items:center}
.footer-bottom{position:absolute;left:0;right:0;bottom:0;height:30px;background:var(--darker)}
.footer-bottom .wrap{height:100%;display:flex;align-items:center;justify-content:space-between;font-size:7px}
.pay{display:flex;gap:4px}
.pay span{width:24px;height:15px;background:#5b5d61;border-radius:2px}
</style>
</head>
<body>
<div class="page">
  <div class="wrap">
    <div class="topbar">
      <div class="welcome">Welcome visitor you can login or create an account</div>
      <div class="links"><span>Wish List (0)</span><span>My Account</span><span>Shopping Cart</span><span>Checkout</span></div>
    </div>

    <header class="header">
      <div class="brand"><span class="brand-dot"></span><span class="brand-name">Crestwave Glow LED</span></div>
      <div class="header-tools">
        <div class="search">
          <div class="search-field">Search</div>
          <div class="search-btn"><svg width="10" height="10" viewBox="0 0 10 10"><circle cx="4" cy="4" r="3" fill="none" stroke="#fff" stroke-width="1.4"/><line x1="6.2" y1="6.2" x2="9" y2="9" stroke="#fff" stroke-width="1.5"/></svg></div>
        </div>
        <div class="cart-btn"><svg width="11" height="10" viewBox="0 0 11 10"><path d="M0 1h2l1.5 5.5h6L11 2.5H3" fill="none" stroke="#fff" stroke-width="1.1"/><circle cx="4" cy="8.6" r="1" fill="#fff"/><circle cx="8.5" cy="8.6" r="1" fill="#fff"/></svg>0 Item(s) - $0.00</div>
      </div>
    </header>

    <div class="navrow">
      <div class="side-title">PRODUCTS</div>
      <nav class="mainnav">
        <a class="active">HOME</a><a>PRODUCTS</a><a>SERVICES</a><a>ABOUT</a><a>FAQ'S</a><a>CONTACT US</a>
      </nav>
    </div>

    <div class="top">
      <ul class="sidebar">
        <li>LED Billboard</li><li>Trusses</li><li>Gas Station lights</li><li>Sound Systems</li>
        <li>Gas Station lights</li><li>LED Billboard</li><li>Trusses</li><li>Gas Station lights</li>
        <li>Sound Systems</li><li>LED Billboard</li><li>Trusses</li><li>Gas Station lights</li>
        <li>Sound Systems</li><li>LED Billboard</li><li>Trusses</li><li>LED Billboard</li>
      </ul>

      <div class="feature">
        <div class="hero" role="img" aria-label="Night video loop of a gas station canopy lit with bright LED lighting">
          <svg class="hero-play" width="42" height="42" viewBox="0 0 42 42"><circle cx="21" cy="21" r="20" fill="rgba(0,0,0,.45)" stroke="#fff" stroke-width="2"/><path d="M17 13l12 8-12 8z" fill="#fff"/></svg>
          <div class="hero-caption">Commercial and Residential Lighting</div>
          <span class="btn">Buy Now</span>
        </div>
        <div class="promos">
          <div class="promo billboards">
            <div class="promo-photo" role="img" aria-label="Outdoor LED billboard screen on a pole"></div>
            <div class="promo-text">
              <h3>LED Billboards:</h3>
              <p>Light Bulb Disposal &amp; Recycling</p>
              <span class="btn">Buy Now</span>
            </div>
          </div>
          <div class="promo gas">
            <div class="promo-photo" role="img" aria-label="Gas station canopy lights glowing at night"></div>
            <div class="promo-text">
              <h3>Gas Station Lights</h3>
              <p>Light Bulb Disposal &amp; Recycling<br>Office, Retail &amp; Standard Lighting</p>
              <span class="btn">Buy Now</span>
            </div>
          </div>
        </div>
      </div>
    </div>

    <div class="section-head">
      <h2>PRODUCTS</h2>
      <div class="arrows">
        <span><svg width="5" height="7" viewBox="0 0 5 7"><path d="M4 0L0 3.5 4 7" fill="none" stroke="#fff" stroke-width="1.2"/></svg></span>
        <span><svg width="5" height="7" viewBox="0 0 5 7"><path d="M1 0l4 3.5L1 7" fill="none" stroke="#fff" stroke-width="1.2"/></svg></span>
      </div>
    </div>

    <div class="products">
      <div class="card">
        <div class="card-photo"><div role="img" aria-label="LED billboard screen on a stand" style="width:110px;height:130px;background:linear-gradient(#1a1a1a,#3a3a3a)"></div></div>
        <div class="card-info"><div><div class="card-name">Product Name</div><div class="card-price">$ 100</div></div><div class="card-cart"><svg width="12" height="11" viewBox="0 0 11 10"><path d="M0 1h2l1.5 5.5h6L11 2.5H3" fill="none" stroke="#fff" stroke-width="1.1"/><circle cx="4" cy="8.6" r="1" fill="#fff"/><circle cx="8.5" cy="8.6" r="1" fill="#fff"/></svg></div></div>
      </div>
      <div class="card">
        <div class="card-photo"><div role="img" aria-label="Stage lighting fixtures on a bar" style="width:120px;height:90px;background:linear-gradient(135deg,#444,#999 50%,#333)"></div></div>
        <div class="card-info"><div><div class="card-name">Product Name</div><div class="card-price">$ 100</div></div><div class="card-cart"><svg width="12" height="11" viewBox="0 0 11 10"><path d="M0 1h2l1.5 5.5h6L11 2.5H3" fill="none" stroke="#fff" stroke-width="1.1"/><circle cx="4" cy="8.6" r="1" fill="#fff"/><circle cx="8.5" cy="8.6" r="1" fill="#fff"/></svg></div></div>
      </div>
      <div class="card">
        <div class="card-photo"><div role="img" aria-label="Aluminium truss system frame" style="width:130px;height:120px;background:linear-gradient(90deg,#bbb,#e9e9e9 50%,#aaa)"></div></div>
        <div class="card-info"><div><div class="card-name">Product Name</div><div class="card-price">$ 100</div></div><div class="card-cart"><svg width="12" height="11" viewBox="0 0 11 10"><path d="M0 1h2l1.5 5.5h6L11 2.5H3" fill="none" stroke="#fff" stroke-width="1.1"/><circle cx="4" cy="8.6" r="1" fill="#fff"/><circle cx="8.5" cy="8.6" r="1" fill="#fff"/></svg></div></div>
      </div>
      <div class="card">
        <div class="card-photo"><div role="img" aria-label="Pair of large loudspeakers" style="width:100px;height:140px;background:linear-gradient(#222,#4a4a4a)"></div></div>
        <div class="card-info"><div><div class="card-name">Product Name</div><div class="card-price">$ 100</div></div><div class="card-cart"><svg width="12" height="11" viewBox="0 0 11 10"><path d="M0 1h2l1.5 5.5h6L11 2.5H3" fill="none" stroke="#fff" stroke-width="1.1"/><circle cx="4" cy="8.6" r="1" fill="#fff"/><circle cx="8.5" cy="8.6" r="1" fill="#fff"/></svg></div></div>
      </div>
    </div>

    <div class="services">
      <div class="service returns">
        <div class="service-icon"><svg width="22" height="20" viewBox="0 0 22 20"><path d="M18 10a7 7 0 1 1-3-5.8" fill="none" stroke="#fff" stroke-width="2"/><path d="M13 1l3 3.5-4 1.5" fill="none" stroke="#fff" stroke-width="2"/></svg></div>
        <div><h4>Returning</h4><p>Easy returns within thirty days<br>on all items with receipt and<br>original packaging.</p></div>
      </div>
      <div class="service warranty">
        <div class="service-icon"><svg width="22" height="20" viewBox="0 0 22 20"><rect x="2" y="2" width="18" height="12" fill="none" stroke="#fff" stroke-width="2"/><path d="M8 18h6M11 14v4" stroke="#fff" stroke-width="2"/></svg></div>
        <div><h4>Warranty</h4><p>Every product is covered by a<br>full warranty on parts and<br>labour for two years.</p></div>
      </div>
      <div class="service shipping">
        <div class="service-icon"><svg width="24" height="18" viewBox="0 0 24 18"><path d="M1 2h13v10H1zM14 6h5l4 4v2h-9z" fill="none" stroke="#fff" stroke-width="1.8"/><circle cx="6" cy="14.5" r="2" fill="#fff"/><circle cx="18" cy="14.5" r="2" fill="#fff"/></svg></div>
        <div><h4>Shipping</h4><p>Fast shipping on all orders with<br>tracking sent straight to your<br>inbox after checkout.</p></div>
      </div>
    </div>
  </div>

  <footer class="footer">
    <div class="wrap footer-cols">
      <div class="footer-col"><h5>Company</h5><ul><li>About Us</li><li>Privacy Policy</li><li>Terms and Conditions</li><li>Sitemap</li></ul></div>
      <div class="footer-col"><h5>Help</h5><ul><li>Orders and Returns</li><li>Shipping Info</li><li>FAQ</li></ul></div>
      <div class="footer-col"><h5>Get in Touch</h5><ul><li>Address: 4820 Glow Park Ave,<br>Suite 12</li><li>Phone: (555) 014-2290</li><li>Email: hello@crestwaveglowled.com</li></ul></div>
      <div class="footer-col newsletter"><h5>Newsletter</h5><p>Get our latest offers and rental<br>news sent to your inbox monthly.</p>
        <div class="subscribe"><div class="field">Enter email address</div><div class="go">Subscribe</div></div></div>
    </div>
    <div class="footer-bottom">
      <div class="wrap">
        <div class="pay"><span></span><span></span><span></span><span></span><span></span><span></span></div>
        <div>Copyright © 2024. All Rights Reserved</div>
      </div>
    </div>
  </footer>
</div>
</body>
</html>
```